Brava Nest (Smart Home, Installation, Repair Industry) (Contest)

Looking for a website design for my company
Services we offer:
Phone Repair
TV Mounting
Security Camera Installation
Networking / Wi-Fi
Smart Home Services
IT Support

Looking for a website similar to trovely.example

Few tabs
About Us
Contact Us
Areas Served
Pricing and Services

```html
<!DOCTYPE html>
<html lang="en">
<head>
<meta charset="utf-8">
<title>Brava Nest — Home maintenance made simple</title>
<link rel="stylesheet" href="https://fonts.googleapis.com/css2?family=Jost:wght@300;400;500;600;700&display=swap">
<style>
:root{
  --orange:#f7931e;
  --ink:#2b2b2b;
  --text:#555;
  --muted:#9a9a9a;
  --line:#e4e4e4;
  --bg:#ffffff;
  --hero-a:#f2f3f5;
  --hero-b:#d9dde3;
  --blue:#1f5fb8;
}
*{box-sizing:border-box;margin:0;padding:0}
html,body{width:1200px;height:3088px;overflow:hidden;background:var(--bg)}
body{position:relative;font-family:"Jost",sans-serif;color:var(--ink)}
.abs{position:absolute}

/* hero */
.hero{position:absolute;left:0;top:0;width:1200px;height:522px;background:linear-gradient(100deg,var(--hero-a) 0%,#e6e8ec 55%,var(--hero-b) 100%)}
.hero-photo{position:absolute;right:0;top:0;width:430px;height:522px;background:linear-gradient(200deg,#e9ecef 0%,#cfd4da 45%,#c9685e 62%,#2f6fcf 85%,#e2e5e9 100%);opacity:.85}
.logo{position:absolute;left:100px;top:22px;font-size:34px;font-weight:700;color:var(--orange);letter-spacing:-.5px}
.nav{position:absolute;top:32px;left:541px;display:flex;gap:0;font-size:14px;font-weight:500}
.nav a{color:var(--ink);text-decoration:none;margin-right:36px}
.nav a.active{color:var(--orange);border-bottom:2px solid var(--orange);padding-bottom:4px}
.hero h1{position:absolute;left:100px;top:196px;font-size:39px;font-weight:400;line-height:42px;color:var(--ink)}
.hero p{position:absolute;left:100px;top:292px;font-size:15px;line-height:21px;color:var(--ink)}
.btn{display:inline-block;background:var(--orange);color:#fff;font-size:15px;text-align:center;text-decoration:none}
.hero .btn{position:absolute;left:100px;top:349px;width:150px;height:53px;line-height:53px}

/* services strip */
.services{position:absolute;top:556px;left:224px;display:flex}
.service{width:125px;text-align:center;font-size:12px;line-height:15px;color:var(--text);border-right:2px solid var(--orange)}
.service:last-child{border-right:none}
.service svg{display:block;margin:0 auto 8px;width:40px;height:34px;stroke:#555;fill:none;stroke-width:1.6}

/* feature */
.feature{position:absolute;left:100px;top:736px;width:1002px;height:261px;border:1px solid var(--orange)}
.feature h2{position:absolute;left:26px;top:50px;font-size:20px;font-weight:500;line-height:26px}
.bullets{position:absolute;left:26px;top:120px;list-style:none;font-size:11.5px;color:var(--text)}
.bullets li{margin-bottom:12px;padding-left:18px;position:relative}
.bullets li::before{content:"";position:absolute;left:0;top:4px;width:8px;height:8px;border-radius:50%;background:var(--orange)}
.house{position:absolute;left:331px;top:0;width:670px;height:259px;background:linear-gradient(180deg,#8fc1e8 0%,#b9d9ef 35%,#d98560 55%,#eeeae4 70%,#6c9a3b 100%)}
.tag{position:absolute;background:#fff;font-size:11px;line-height:14px;text-align:center;color:var(--text);padding:4px 8px;border-radius:2px}
.pin{position:absolute;width:12px;height:12px;border-radius:50%;background:#4a9ef0;border:2px solid #fff}

/* section headings */
.sec-title{position:absolute;left:100px;font-size:20px;font-weight:500}

/* technicians */
.card{position:absolute;top:1115px;width:319px;height:185px;border:1px solid var(--orange)}
.avatar{position:absolute;left:17px;top:14px;width:46px;height:46px;border-radius:50%;background:linear-gradient(135deg,#b48a6d,#4f3a2e)}
.tech-name{position:absolute;left:72px;top:20px;font-size:11.5px;line-height:14px;color:var(--ink)}
.tech-name b{font-weight:600}
.badge{position:absolute;right:18px;top:20px;width:36px;height:14px;border-radius:3px;background:#dadada}
.quote{position:absolute;left:17px;top:74px;width:285px;font-size:11.5px;line-height:18px;color:var(--text)}
.reviewer{position:absolute;left:17px;bottom:18px;font-size:11.5px;color:var(--text)}
.stars{position:absolute;right:18px;bottom:18px;font-size:11px;letter-spacing:3px;color:var(--orange)}
.arrow{position:absolute;left:1116px;width:24px;height:24px;border:1px solid #ddd;border-radius:50%;display:flex;align-items:center;justify-content:center}
.arrow svg{width:8px;height:8px;stroke:#444;fill:none;stroke-width:1.6}

/* blog */
.post{position:absolute;top:1417px;width:238px}
.post .thumb{height:110px}
.post h3{margin-top:18px;font-size:14.5px;font-weight:400;line-height:19px;color:var(--ink)}
.post p{margin-top:10px;font-size:11.5px;line-height:15px;color:var(--text)}
.post time{display:block;margin-top:9px;font-size:11.5px;color:var(--muted)}

/* brands */
.brands{position:absolute;left:100px;width:1000px;display:flex;align-items:center;color:#aab0b8;font-weight:700}
.more{position:absolute;left:944px;top:1790px;width:152px;height:44px;border:1px solid var(--orange);font-size:12px;color:#b8b8b8;text-align:center;line-height:44px}

/* cities */
.city-col{position:absolute;top:2176px;width:125px;font-size:11.5px;line-height:20px;color:var(--text)}
.city-col div{border-bottom:1px solid var(--line);padding-bottom:7px;margin-bottom:6px}
.city-col div:last-child{border-bottom:none}

/* cta */
.cta{position:absolute;left:100px;top:2395px;width:1002px;height:333px;border:1px solid var(--orange)}
.cta h2{position:absolute;left:44px;top:70px;font-size:20px;font-weight:500;line-height:25px}
.cta p{position:absolute;left:44px;top:138px;font-size:11.5px;line-height:16px;color:var(--muted)}
.cta .btn{position:absolute;left:44px;top:186px;width:130px;height:41px;line-height:41px;font-size:13px}
.cta-photo{position:absolute;left:341px;top:0;width:660px;height:331px;background:linear-gradient(90deg,#e9e4dc 0%,#d6d2cc 20%,#2d4a78 45%,#7f8f9e 65%,#2a3f66 100%)}

/* footer */
.f-col{position:absolute;top:2806px;font-size:11px;line-height:23.4px;color:var(--muted)}
.f-col h4{font-size:11px;font-weight:600;color:var(--ink);margin-bottom:4px}
.email-field{position:absolute;left:748px;top:2846px;width:228px;height:28px;border-bottom:1px solid #888;font-size:12px;color:var(--text);line-height:28px}
.subscribe{position:absolute;left:989px;top:2838px;width:103px;height:36px;line-height:36px;font-size:13px}
.social{position:absolute;top:2915px;width:26px;height:26px;border-radius:50%;background:var(--orange)}
.copy-rule{position:absolute;left:108px;top:3040px;width:984px;height:1px;background:var(--orange)}
.copyright{position:absolute;top:3056px;left:0;width:1200px;text-align:center;font-size:9px;color:var(--muted)}
</style>
</head>
<body>

<header class="hero">
  <div class="hero-photo" role="img" aria-label="Technician in cap and safety glasses working on a ladder with a blue bucket"></div>
  <div class="logo">Brava Nest</div>
  <nav class="nav">
    <a class="active" href="#">Home</a><a href="#">About Us</a><a href="#">Contact Us</a><a href="#">Areas Served</a><a href="#">Services</a><a href="#">Pricing</a>
  </nav>
  <h1>Home maintenance<br>made simple with Brava Nest</h1>
  <p>The best technicians in<br>your nearby area.</p>
  <a class="btn" href="#">Book a Service</a>
</header>

<section class="services">
  <div class="service"><svg viewBox="0 0 40 34"><rect x="3" y="3" width="34" height="22" rx="1"/><path d="M14 31h12M20 25v6"/></svg>TV<br>Mounting</div>
  <div class="service"><svg viewBox="0 0 40 34"><rect x="7" y="3" width="26" height="28" rx="2"/><circle cx="20" cy="19" r="6"/><path d="M7 9h26"/></svg>Security Camera<br>Installation</div>
  <div class="service"><svg viewBox="0 0 40 34"><rect x="3" y="10" width="34" height="20" rx="2"/><path d="M14 10V5h12v5M3 19h34"/><rect x="16" y="16" width="8" height="6"/></svg>Wifi<br>Networking</div>
  <div class="service"><svg viewBox="0 0 40 34"><rect x="12" y="2" width="16" height="30" rx="2"/><path d="M18 28h4"/></svg>Phone<br>Repair</div>
  <div class="service"><svg viewBox="0 0 40 34"><path d="M3 15L20 3l17 12v17H3z"/><path d="M13 20a10 10 0 0 1 14 0M16 23a5 5 0 0 1 8 0"/><circle cx="20" cy="26" r="1"/></svg>Smart Home<br>Installation</div>
  <div class="service"><svg viewBox="0 0 40 34"><path d="M3 13L20 3l17 10"/><rect x="7" y="13" width="26" height="19"/><path d="M7 19h26M7 25h26"/></svg>IT<br>Support</div>
</section>

<section class="feature">
  <h2>A simple way to take care of<br>everything</h2>
  <ul class="bullets">
    <li>Lorem ipsum dolor sit amet, consectetur.</li>
    <li>Lorem ipsum dolor sit amet, consectetur.</li>
    <li>Lorem ipsum dolor sit amet, consectetur.</li>
  </ul>
  <div class="house" role="img" aria-label="Modern two-storey house with red walls, garage and trees">
    <div class="tag" style="left:233px;top:8px">Wifi<br>Networking</div><div class="pin" style="left:297px;top:56px"></div>
    <div class="tag" style="left:346px;top:27px">Smart Home<br>Installation</div><div class="pin" style="left:357px;top:76px"></div>
    <div class="tag" style="left:480px;top:47px">TV<br>Mounting</div><div class="pin" style="left:491px;top:95px"></div>
    <div class="tag" style="left:158px;top:70px;font-size:9.5px;line-height:13px">Security Camera<br>Installation</div><div class="pin" style="left:223px;top:118px"></div>
    <div class="tag" style="left:115px;top:153px">IT<br>Support</div><div class="pin" style="left:165px;top:198px"></div>
  </div>
</section>

<h2 class="sec-title" style="top:1073px">Our top technicians are in your nearby!</h2>
<article class="card" style="left:100px">
  <div class="avatar" role="img" aria-label="Technician portrait"></div>
  <div class="tech-name"><b>John</b><br>Brava Nest technician</div><div class="badge"></div>
  <p class="quote">“Lorem ipsum dolor sit amet, consectetur adipisic-ing elit, sed do eiusmod tempor incididunt ut labore et dolore magna aliqua.”</p>
  <div class="reviewer">Adrienne | Los Angeles, CA</div><div class="stars">★★★★★</div>
</article>
<article class="card" style="left:436px">
  <div class="avatar" role="img" aria-label="Technician portrait" style="background:linear-gradient(135deg,#e0d6cc,#5a4a3e)"></div>
  <div class="tech-name"><b>Joe</b><br>Brava Nest technician</div><div class="badge"></div>
  <p class="quote">“Lorem ipsum dolor sit amet, consectetur adip-isicing elit, sed do eiusmod tempor incididunt ut labore et dolore magna aliqua.”</p>
  <div class="reviewer">Donnie | Colton, CA</div><div class="stars">★★★★★</div>
</article>
<article class="card" style="left:773px">
  <div class="avatar" role="img" aria-label="Technician portrait" style="background:linear-gradient(135deg,#c69a6a,#2e2a28)"></div>
  <div class="tech-name"><b>Sam</b><br>Brava Nest technician</div><div class="badge"></div>
  <p class="quote">“Lorem ipsum dolor sit amet, consectetur adipisicing elit, sed do eiusmod tempor incididunt ut labore et dolore magna aliqua.”</p>
  <div class="reviewer">Sriram | Houston, TX</div><div class="stars">★★★★★</div>
</article>
<div class="arrow" style="top:1192px"><svg viewBox="0 0 8 8"><path d="M2 1l3 3-3 3"/></svg></div>

<h2 class="sec-title" style="top:1375px">The Brava Nest blog</h2>
<article class="post" style="left:100px"><div class="thumb" role="img" aria-label="Desk phone on a sunlit office desk" style="background:linear-gradient(120deg,#f3e1b4,#d9b36a 50%,#8a7c6a)"></div><h3>Lorem ipsum dolor sit amet,<br>consectetur adipiscing</h3><p>Consectetur adipiscing elit, sed do<br>eiusmod tempor incididunt...</p><time>April 2020</time></article>
<article class="post" style="left:352px"><div class="thumb" role="img" aria-label="Two customers talking with a technician" style="background:linear-gradient(120deg,#c9c3bb,#e6e2dc 50%,#3d5a85)"></div><h3>Lorem ipsum dolor sit amet, con-<br>sectetur adipiscing</h3><p>Consectetur adipiscing elit, sed<br>do eiusmod tempor incididunt...</p><time>April 2020</time></article>
<article class="post" style="left:605px"><div class="thumb" role="img" aria-label="Technicians mounting a screen on a wall" style="background:linear-gradient(120deg,#2e3f63,#8796a8 50%,#dcd8d2)"></div><h3>Lorem ipsum dolor sit amet,<br>consectetur adipiscing</h3><p>Consectetur adipiscing elit, sed do<br>eiusmod tempor incididunt...</p><time>April 2020</time></article>
<article class="post" style="left:857px"><div class="thumb" role="img" aria-label="Technician speaking with two customers" style="background:linear-gradient(120deg,#3d5a85,#d8d2ca 50%,#c9c3bb)"></div><h3>Lorem ipsum dolor sit amet,<br>consectetur adipiscing</h3><p>Consectetur adipiscing elit, sed do<br>eiusmod tempor incididunt...</p><time>April 2020</time></article>
<div class="arrow" style="top:1460px"><svg viewBox="0 0 8 8"><path d="M2 1l3 3-3 3"/></svg></div>

<h2 class="sec-title" style="top:1743px">Trusted By</h2>
<div class="brands" style="top:1794px;font-size:24px">
  <span style="width:210px">Norvale</span><span style="width:210px">Quinta</span><span style="width:210px">Orbix</span><span>Safehaven</span>
</div>
<div class="more">And many more</div>

<h2 class="sec-title" style="top:1943px">Featured In</h2>
<div class="brands" style="top:1982px;font-size:21px;justify-content:space-between;width:985px">
  <span>The Daily Ledger</span><span>Market Wire</span><span>TechPulse</span><span>Bright Capital</span><span>Metro Courier</span><span>Startup Signal</span>
</div>

<h2 class="sec-title" style="top:2125px">Cities where Brava Nest is available:</h2>
<div class="city-col" style="left:100px"><div>Arizona<br>Phoenix</div><div>Colorado<br>Denver</div></div>
<div class="city-col" style="left:275px"><div>Florida<br>Miami<br>Orlando<br>Tampa</div><div>Georgia<br>Atlanta</div></div>
<div class="city-col" style="left:450px"><div>Illinois<br>Chicago</div><div>Massachusetts<br>Boston</div><div>Nevada<br>Las Vegas</div></div>
<div class="city-col" style="left:625px"><div>North Carolina<br>Charlotte</div><div>Pennsylvania<br>Philadelphia</div></div>
<div class="city-col" style="left:800px"><div>Texas<br>Austin<br>Dallas<br>Houston<br>San Antonio</div></div>
<div class="city-col" style="left:976px"><div>Washington D.C.<br>Washington, D.C.</div></div>

<section class="cta">
  <h2>Thinking of getting<br>started?</h2>
  <p>Repair or install<br>a device today.</p>
  <a class="btn" href="#">Book a Service</a>
  <div class="cta-photo" role="img" aria-label="Technician mounting a large TV screen on a wall"></div>
</section>

<footer>
  <div class="f-col" style="left:108px"><h4>Company</h4>Home<br>About Us<br>Areas Served<br>Services<br>Pricing<br>Contact Us</div>
  <div class="f-col" style="left:268px"><h4>Resources</h4>TV Mounting<br>Camera Installation<br>Wifi Networking<br>Phone Repair<br>Smart Home Installation</div>
  <div class="f-col" style="left:428px"><h4>Partnerships</h4>Orbix<br>Safehaven</div>
  <div class="f-col" style="left:588px"><h4>Legals</h4>Privacy<br>Terms<br>Brava Nest Terms<br>Guarantee</div>
  <div class="f-col" style="left:748px;top:2814px"><h4>Stay Connected</h4></div>
  <div class="email-field">Enter email</div>
  <a class="btn subscribe" href="#">Subscribe</a>
  <span class="social" style="left:748px"></span><span class="social" style="left:791px"></span><span class="social" style="left:834px"></span>
  <div class="f-col" style="left:748px;top:2971px;color:var(--ink)">support@bravanest.example</div>
  <div class="copy-rule"></div>
  <div class="copyright">© 2020 Brava Nest. All Right Reserved.</div>
</footer>

</body>
</html>
```